Byteway Tech Services Flyer

I have a retail Computer Store that I want to promote in the local area.
The target market is seniors aged between 40-80 year olds. I need to create a flyer for the business to do a flyer drop to homes and business advertising the business & services we offer. I would also like to drop this on our socials for online target ads.
Store Name: Byteway Tech systems Address: 17 Larkspur Road, MERROWDALE Victoria 3999 Phone Number: (03) 9521 6408 Target Audience: older generation between 40 - 90 year olds Services offered: Retail Sales & Service, Complete Workshop Facilities, Cloud services, Deskly 240 Experts, Network & Wireless Products, Managed Services, PC & Laptop Sales, Custom Built Computers Vendors: Veltrix, QORNL, Parvanix Partner, Olex, Brimo, Tovi & Rune Reseller Please keep it to A1 size and double sided with options to go A3 o A4 later.

Target Market(s)

Residential home users

Industry/Entity Type

www.bytewaytech.com.au

Font styles to use
Sans Serif

Colors
0054AA
0677BA
7BADD7
CADEEF
E8F1F8

Requirements
Must have
• Simple target is the elderly population

```html
<!DOCTYPE html>
<html lang="en">
<head>
<meta charset="utf-8">
<title>Byteway Tech Systems – Flyer</title>
<link href="https://fonts.googleapis.com/css2?family=Montserrat:wght@400;500;600;700;800&display=swap" rel="stylesheet">
<style>
  :root {
    --deep-blue: #0054AA;
    --mid-blue: #0677BA;
    --soft-blue: #7BADD7;
    --pale-blue: #CADEEF;
    --mist-blue: #E8F1F8;
    --footer-grey: #6a6a6a;
    --text-dark: #2b2b2b;
    --backdrop: #e4e4e4;
    --white: #ffffff;
  }
  * { box-sizing: border-box; margin: 0; padding: 0; }
  html, body { width: 723px; height: 1200px; overflow: hidden; }
  body {
    background: var(--backdrop);
    font-family: "Montserrat", Arial, sans-serif;
    position: relative;
  }
  .flyer-page {
    position: absolute;
    left: 154px;
    width: 414px;
    height: 582px;
    background: var(--white);
    box-shadow: 0 3px 10px rgba(0,0,0,0.25);
    overflow: hidden;
  }
  .flyer-front { top: 10px; }
  .flyer-back { top: 606px; }

  /* Header */
  .brand-header {
    position: absolute; top: 0; left: 0; width: 100%; height: 56px;
    display: flex; align-items: center; gap: 10px; padding-left: 18px;
  }
  .brand-square { width: 22px; height: 22px; background: var(--deep-blue); border-radius: 3px; }
  .brand-name {
    font-weight: 600; font-size: 21px; letter-spacing: 4px;
    color: var(--deep-blue); text-transform: uppercase;
  }
  .header-rule {
    position: absolute; top: 58px; left: 0; width: 300px; height: 5px;
    background: linear-gradient(90deg, var(--mid-blue), var(--soft-blue));
  }

  /* Photo areas */
  .photo-area { position: absolute; left: 0; width: 100%; display: block; }
  .flyer-front .photo-area { top: 66px; height: 236px; }
  .flyer-back .photo-area { top: 0; height: 303px; }

  /* Blue title band */
  .title-band {
    position: absolute; left: 0; width: 100%;
    background: linear-gradient(180deg, var(--mid-blue) 0%, var(--deep-blue) 100%);
    color: var(--white); text-align: center;
  }
  .flyer-front .title-band { top: 302px; height: 90px; padding-top: 6px; }
  .store-title {
    font-weight: 800; font-size: 39px; line-height: 40px;
    text-transform: uppercase; letter-spacing: 0.5px;
  }

  /* Services */
  .services-tab { position: absolute; top: 392px; left: 0; width: 100%; height: 26px; }
  .services-tab svg { position: absolute; top: 0; left: 0; }
  .services-label {
    position: absolute; top: 4px; width: 100%; text-align: center;
    font-size: 14px; font-weight: 700; color: var(--mid-blue); letter-spacing: 0.3px;
  }
  .service-columns {
    position: absolute; top: 428px; left: 22px; right: 12px;
    display: grid; grid-template-columns: 1fr 1fr; column-gap: 14px;
  }
  .service-list { list-style: none; }
  .service-list.first-col { border-right: 2px solid var(--mid-blue); padding-right: 6px; }
  .service-item {
    display: flex; gap: 8px; align-items: flex-start;
    font-size: 10.5px; font-weight: 700; color: var(--text-dark);
    text-transform: uppercase; line-height: 13px; margin-bottom: 6px;
  }
  .tick { flex: 0 0 10px; margin-top: 1px; }

  /* Footer */
  .footer-rule {
    position: absolute; left: 0; width: 100%; top: 526px; height: 6px;
    background: linear-gradient(90deg, var(--deep-blue), var(--soft-blue), var(--deep-blue));
  }
  .contact-footer {
    position: absolute; left: 0; bottom: 0; width: 100%; height: 50px;
    background: var(--footer-grey); color: var(--white); text-align: center; padding-top: 7px;
  }
  .contact-address {
    font-size: 9px; font-weight: 600; text-transform: uppercase;
    display: flex; justify-content: center; align-items: center; gap: 3px;
  }
  .contact-phone {
    font-size: 18px; font-weight: 700; margin-top: 1px;
    display: flex; justify-content: center; align-items: center; gap: 6px;
  }

  /* Back side */
  .flyer-back .title-band { top: 303px; height: 89px; padding-top: 18px; }
  .vendors-kicker { font-size: 22px; font-weight: 500; line-height: 24px; text-transform: uppercase; }
  .vendors-title { font-size: 23px; font-weight: 800; line-height: 26px; text-transform: uppercase; }
  .vendor-grid {
    position: absolute; top: 408px; left: 17px; right: 17px;
    display: grid; grid-template-columns: repeat(3, 1fr); gap: 7px;
  }
  .vendor-tile {
    height: 46px; border: 1px solid #bdbdbd; background: var(--white);
    display: flex; align-items: center; justify-content: center; gap: 12px;
    font-size: 18px; font-weight: 700; color: var(--deep-blue); letter-spacing: 0.5px;
  }
  .vendor-tile .dark { color: var(--text-dark); }
</style>
</head>
<body>

<section class="flyer-page flyer-front">
  <header class="brand-header">
    <span class="brand-square"></span>
    <span class="brand-name">Byteway Tech</span>
  </header>
  <div class="header-rule"></div>

  <svg class="photo-area" role="img" aria-label="Photo: laptops on display tables in a computer store" viewBox="0 0 414 236" preserveAspectRatio="none">
    <defs>
      <linearGradient id="storeLeft" x1="0" y1="0" x2="1" y2="1">
        <stop offset="0" stop-color="#c9d3de"/>
        <stop offset="0.5" stop-color="#7d8fa6"/>
        <stop offset="1" stop-color="#e3ddd4"/>
      </linearGradient>
      <linearGradient id="storeRight" x1="0" y1="0" x2="1" y2="1">
        <stop offset="0" stop-color="#b7a88f"/>
        <stop offset="0.5" stop-color="#dfe3ea"/>
        <stop offset="1" stop-color="#9fb5cf"/>
      </linearGradient>
    </defs>
    <polygon points="0,0 285,0 178,236 0,236" fill="url(#storeLeft)"/>
    <polygon points="305,-20 414,-20 414,236 198,236" fill="url(#storeRight)"/>
    <polygon points="285,0 322,-40 210,236 178,236" fill="#ffffff"/>
  </svg>

  <div class="title-band">
    <h1 class="store-title">Byteway<br>Tech Systems</h1>
  </div>

  <div class="services-tab">
    <svg width="414" height="26" viewBox="0 0 414 26">
      <polyline points="0,2 112,2 128,22 286,22 302,2 414,2" fill="none" stroke="#0677BA" stroke-width="2"/>
    </svg>
    <div class="services-label">SERVICES OFFERED:</div>
  </div>

  <div class="service-columns">
    <ul class="service-list first-col">
      <li class="service-item"><svg class="tick" width="10" height="10" viewBox="0 0 10 10"><circle cx="5" cy="5" r="5" fill="#0677BA"/><polyline points="2.6,5.2 4.3,6.8 7.4,3.4" fill="none" stroke="#fff" stroke-width="1.4"/></svg>Retail Sales &amp; Service</li>
      <li class="service-item"><svg class="tick" width="10" height="10" viewBox="0 0 10 10"><circle cx="5" cy="5" r="5" fill="#0677BA"/><polyline points="2.6,5.2 4.3,6.8 7.4,3.4" fill="none" stroke="#fff" stroke-width="1.4"/></svg>Complete Workshop Facilities</li>
      <li class="service-item"><svg class="tick" width="10" height="10" viewBox="0 0 10 10"><circle cx="5" cy="5" r="5" fill="#0677BA"/><polyline points="2.6,5.2 4.3,6.8 7.4,3.4" fill="none" stroke="#fff" stroke-width="1.4"/></svg>Cloud Services</li>
      <li class="service-item"><svg class="tick" width="10" height="10" viewBox="0 0 10 10"><circle cx="5" cy="5" r="5" fill="#0677BA"/><polyline points="2.6,5.2 4.3,6.8 7.4,3.4" fill="none" stroke="#fff" stroke-width="1.4"/></svg>Deskly 240 Experts</li>
    </ul>
    <ul class="service-list">
      <li class="service-item"><svg class="tick" width="10" height="10" viewBox="0 0 10 10"><circle cx="5" cy="5" r="5" fill="#0677BA"/><polyline points="2.6,5.2 4.3,6.8 7.4,3.4" fill="none" stroke="#fff" stroke-width="1.4"/></svg>Network &amp; Wireless Products</li>
      <li class="service-item"><svg class="tick" width="10" height="10" viewBox="0 0 10 10"><circle cx="5" cy="5" r="5" fill="#0677BA"/><polyline points="2.6,5.2 4.3,6.8 7.4,3.4" fill="none" stroke="#fff" stroke-width="1.4"/></svg>Managed Services</li>
      <li class="service-item"><svg class="tick" width="10" height="10" viewBox="0 0 10 10"><circle cx="5" cy="5" r="5" fill="#0677BA"/><polyline points="2.6,5.2 4.3,6.8 7.4,3.4" fill="none" stroke="#fff" stroke-width="1.4"/></svg>PC &amp; Laptop Sales</li>
    </ul>
  </div>

  <div class="footer-rule"></div>
  <footer class="contact-footer">
    <p class="contact-address"><svg width="9" height="10" viewBox="0 0 9 10"><path d="M4.5 0.5a3 3 0 0 1 3 3c0 2.2-3 5-3 5s-3-2.8-3-5a3 3 0 0 1 3-3z" fill="#7BADD7"/><circle cx="4.5" cy="3.5" r="1" fill="#6a6a6a"/></svg>17 Larkspur Road, MERROWDALE Victoria 3999</p>
    <p class="contact-phone"><svg width="14" height="14" viewBox="0 0 14 14"><circle cx="7" cy="7" r="7" fill="#0677BA"/><path d="M4.6 3.6l1.4 1.6-0.8 1c0.5 1 1.3 1.8 2.3 2.3l1-0.8 1.6 1.4-0.9 1.2c-2.9-0.3-5.6-3-5.8-5.8z" fill="#fff"/></svg>(03) 9521 6408</p>
  </footer>
</section>

<section class="flyer-page flyer-back">
  <svg class="photo-area" role="img" aria-label="Photo: store staff helping customers choose a laptop" viewBox="0 0 414 303" preserveAspectRatio="none">
    <defs>
      <linearGradient id="staffLeft" x1="0" y1="0" x2="1" y2="1">
        <stop offset="0" stop-color="#3a5f9a"/>
        <stop offset="0.45" stop-color="#9db7d8"/>
        <stop offset="1" stop-color="#e8ecf1"/>
      </linearGradient>
      <linearGradient id="staffRight" x1="0" y1="0" x2="1" y2="1">
        <stop offset="0" stop-color="#dfe4ea"/>
        <stop offset="0.5" stop-color="#b8c6d8"/>
        <stop offset="1" stop-color="#8a8f98"/>
      </linearGradient>
    </defs>
    <polygon points="0,0 318,0 184,303 0,303" fill="url(#staffLeft)"/>
    <polygon points="338,0 414,0 414,303 204,303" fill="url(#staffRight)"/>
    <polygon points="318,0 338,0 204,303 184,303" fill="#ffffff"/>
  </svg>

  <div class="title-band">
    <p class="vendors-kicker">Custom Built</p>
    <h2 class="vendors-title">Computers Vendors:</h2>
  </div>

  <div class="vendor-grid">
    <div class="vendor-tile">VELTRIX</div>
    <div class="vendor-tile"><span class="dark">QORNL</span></div>
    <div class="vendor-tile"><span class="dark">Parvanix</span></div>
    <div class="vendor-tile">Venquo</div>
    <div class="vendor-tile">Brimo</div>
    <div class="vendor-tile"><span class="dark">Rune</span><span>Tovi</span></div>
  </div>

  <div class="footer-rule"></div>
  <footer class="contact-footer">
    <p class="contact-address"><svg width="9" height="10" viewBox="0 0 9 10"><path d="M4.5 0.5a3 3 0 0 1 3 3c0 2.2-3 5-3 5s-3-2.8-3-5a3 3 0 0 1 3-3z" fill="#7BADD7"/><circle cx="4.5" cy="3.5" r="1" fill="#6a6a6a"/></svg>17 Larkspur Road, MERROWDALE Victoria 3999</p>
    <p class="contact-phone"><svg width="14" height="14" viewBox="0 0 14 14"><circle cx="7" cy="7" r="7" fill="#0677BA"/><path d="M4.6 3.6l1.4 1.6-0.8 1c0.5 1 1.3 1.8 2.3 2.3l1-0.8 1.6 1.4-0.9 1.2c-2.9-0.3-5.6-3-5.8-5.8z" fill="#fff"/></svg>(03) 9521 6408</p>
  </footer>
</section>

</body>
</html>
```